Zanquorra Business Card Design

Zanquorra is a small and new restaurant/ bar location in Hong Kong. The name "Djibouti" derives from an African country. There is no specific reason behind other than the fact, that the bar is somewhat inspired by African elements (only inspired but not purely based on African cuisine etc.).

The bar is somewhat a fusion of African, Mediterranean and Oriental (Old French Vietnam) elements.

However, it is very imperative to stress, that the overall look and feel of Zanquorra is a very high end cocktail lounge/ bar location. The bar is tucked away in a hidden alley, so people will have to know about it. The idea is to send the consumer off in an Escape or hidden remote location where they are at ease in a hip, stylish and trendy environment.

The card needs to feel high-end.

Final logo artwork has been attached and also pictures of the bar/ restaurant itself. The logo ie monkey head cannot be modified. However, the background color and the color of the type "ZANQUORRA" can be changed.

The following details need to fit onto the business card. Of course they can be arranged to your liking:

LOGO

Colin Vey
Partner

+852 97035164
xxx@zanquorra.com
www.zanquorra.com
7C, Brennick Road, Wan Chai, Hong Kong

```html
<!DOCTYPE html>
<html lang="en">
<head>
<meta charset="utf-8">
<title>Zanquorra Business Card</title>
<link rel="stylesheet" href="https://fonts.googleapis.com/css2?family=PT+Sans:wght@400;700&display=swap">
<style>
  :root {
    --page-bg: #ffffff;
    --card-black: #0d0d0d;
    --card-charcoal: #2c2c2c;
    --card-sheen: #3d3d3d;
    --brand-blue: #1b9ad6;
    --title-gold: #f0b549;
    --text-white: #ffffff;
    --mark-fill: #241a14;
    --mark-ring: #ffffff;
  }
  * { box-sizing: border-box; margin: 0; padding: 0; }
  html, body {
    width: 1200px;
    height: 968px;
    overflow: hidden;
    background: var(--page-bg);
  }
  .canvas {
    position: relative;
    width: 1200px;
    height: 968px;
    font-family: "PT Sans", sans-serif;
  }

  /* Front card (landscape) */
  .card-front {
    position: absolute;
    left: 378px;
    top: 435px;
    width: 788px;
    height: 449px;
    z-index: 1;
    overflow: hidden;
    background: linear-gradient(180deg, var(--card-black) 0%, var(--card-charcoal) 45%, var(--card-charcoal) 60%, var(--card-black) 100%);
  }
  .card-front .texture {
    position: absolute;
    inset: 0;
    background: radial-gradient(ellipse at 50% 45%, rgba(255,255,255,0.06) 0%, rgba(0,0,0,0) 70%);
  }
  .card-front .brand-mark {
    position: absolute;
    left: 286px;
    top: 44px;
    width: 226px;
    height: 226px;
  }
  .card-front .brand-name {
    position: absolute;
    left: 0;
    right: 0;
    top: 310px;
    text-align: center;
    font-size: 66px;
    font-weight: 700;
    letter-spacing: 3px;
    color: var(--brand-blue);
  }

  /* Back card (portrait, contact details) */
  .card-back {
    position: absolute;
    left: 34px;
    top: 18px;
    width: 449px;
    height: 787px;
    z-index: 2;
    overflow: hidden;
    background: linear-gradient(90deg, var(--card-black) 0%, var(--card-charcoal) 40%, var(--card-sheen) 58%, var(--card-charcoal) 72%, var(--card-black) 100%);
  }
  .card-back .faint-motif {
    position: absolute;
    left: 0;
    top: 0;
    width: 260px;
    height: 520px;
    background: radial-gradient(ellipse at 60% 35%, rgba(255,255,255,0.08) 0%, rgba(255,255,255,0) 70%);
  }
  .card-back .brand-mark {
    position: absolute;
    left: 209px;
    top: 105px;
    width: 150px;
    height: 150px;
  }
  .card-back .brand-name {
    position: absolute;
    left: 140px;
    width: 290px;
    top: 276px;
    text-align: center;
    font-size: 44px;
    font-weight: 700;
    letter-spacing: 2px;
    color: var(--brand-blue);
  }
  .contact {
    position: absolute;
    right: 38px;
    top: 458px;
    text-align: right;
    color: var(--text-white);
  }
  .contact .person-name {
    font-size: 29px;
    line-height: 36px;
  }
  .contact .person-title {
    font-size: 24px;
    line-height: 30px;
    color: var(--title-gold);
    margin-bottom: 46px;
  }
  .contact .detail {
    font-size: 24px;
    line-height: 35.5px;
  }
</style>
</head>
<body>
<div class="canvas">

  <section class="card-front">
    <div class="texture" role="img" aria-label="Subtle dark ornamental background pattern"></div>
    <svg class="brand-mark" viewBox="0 0 226 226" aria-hidden="true">
      <circle cx="113" cy="113" r="110" fill="var(--mark-fill)" stroke="var(--mark-ring)" stroke-width="5"/>
    </svg>
    <div class="brand-name">ZANQUORRA</div>
  </section>

  <section class="card-back">
    <div class="faint-motif" role="img" aria-label="Faint dark decorative motif"></div>
    <svg class="brand-mark" viewBox="0 0 150 150" aria-hidden="true">
      <circle cx="75" cy="75" r="72" fill="var(--mark-fill)" stroke="var(--mark-ring)" stroke-width="4"/>
    </svg>
    <div class="brand-name">ZANQUORRA</div>

    <div class="contact">
      <p class="person-name">Colin Vey</p>
      <p class="person-title">Partner</p>
      <p class="detail">+852 97035164</p>
      <p class="detail">colin@zanquorra.com</p>
      <p class="detail">www.zanquorra.com</p>
      <p class="detail">7C, Brennick Road, Wan Chai,</p>
      <p class="detail">Hong Kong</p>
    </div>
  </section>

</div>
</body>
</html>
```